The Amber Lantern illustrated story adaptation design

I need a graphic-novel-style design of the 10-page story, “The Amber Lantern.” This will appear in a collection of graphic-novel-style adaptations of stories which I am posting online (and printing) in May.

Half of the files are on filecrate (under "6 images"):

https://www.filecrate-share.net/s/q3mz81kd0tx5pw2/page%20thumbs_0full_01.jpg?dl=0

Target Market(s)

comic book readers, graphic novel readers, young adult readers

Industry/Entity Type

Publishing

Font styles to use
Serif
Other font styles liked:
• Caslon Anitque, Californian FB, 1584 Pragmatica Lima

Colors

Designer to choose colors to be used in the design.

Requirements
Must have
• A bold design scheme !! The art and text are solid, but they certainly need a clever design concept that can bind the project together.
Nice to have
• An inviting, reader-friendly background of some kind (I offer suggestions in my notes).
Should not have
• Hard-to-read graphics

```html
<!DOCTYPE html>
<html lang="en">
<head>
<meta charset="utf-8">
<title>The Amber Lantern — Page</title>
<link rel="stylesheet" href="https://fonts.googleapis.com/css2?family=Alegreya:wght@400&family=Alegreya+SC:wght@400&display=swap">
<style>
  :root {
    --parchment: #fbe7d2;
    --parchment-edge: #f1c8b2;
    --ink: #1a1612;
    --frame: #0b0b0b;
    --caption: #fbf632;
    --teal-dark: #1d2a2e;
    --teal-mid: #3f565c;
    --teal-light: #6f8d93;
    --mauve: #5b4a5e;
    --wine: #5a2a32;
  }
  * { margin: 0; padding: 0; box-sizing: border-box; }
  html, body { width: 960px; height: 1200px; overflow: hidden; }
  body {
    position: relative;
    background: radial-gradient(ellipse 75% 70% at 50% 48%, var(--parchment) 60%, var(--parchment-edge) 100%);
    font-family: "Alegreya", Georgia, serif;
    color: var(--ink);
  }
  .story-title {
    position: absolute;
    left: 597px; top: 54px;
    font-family: "Alegreya SC", Georgia, serif;
    font-size: 18px;
    letter-spacing: 0.27em;
    font-weight: 400;
    text-transform: uppercase;
  }
  .panel { position: absolute; }
  .panel > svg.frame { position: absolute; inset: 0; width: 100%; height: 100%; }
  .panel .art { position: absolute; }

  .panel-city { left: 82px; top: 138px; width: 796px; height: 356px; }
  .panel-city .art {
    left: 9px; top: 10px; right: 9px; bottom: 10px;
    background:
      radial-gradient(ellipse 22% 18% at 30% 38%, rgba(180,196,196,0.55), transparent 70%),
      radial-gradient(ellipse 14% 10% at 48% 48%, rgba(150,70,60,0.45), transparent 70%),
      radial-gradient(ellipse 40% 12% at 60% 70%, rgba(110,45,55,0.55), transparent 70%),
      radial-gradient(ellipse 30% 20% at 85% 45%, rgba(90,110,120,0.5), transparent 70%),
      linear-gradient(180deg, #2a383e 0%, #415860 30%, #34474c 48%, #3c3a40 62%, #2b3638 78%, #1c2426 100%);
  }
  .caption-lead {
    position: absolute;
    left: 96px; top: 150px; width: 310px; height: 54px;
  }
  .caption-lead svg { position: absolute; inset: 0; width: 100%; height: 100%; }
  .caption-lead span {
    position: relative;
    display: flex; height: 100%;
    align-items: center; justify-content: center;
    font-size: 19px;
  }
  .page-mark {
    position: absolute;
    width: 22px; height: 22px;
    border: 1.5px solid #e8eef0;
    border-radius: 50%;
    color: #e8eef0;
    font-size: 13px;
    line-height: 19px;
    text-align: center;
  }
  .panel-city .page-mark { right: 22px; bottom: 20px; }
  .panel-tower .page-mark { right: 16px; bottom: 14px; width: 18px; height: 18px; font-size: 11px; line-height: 15px; }

  .narration {
    position: absolute;
    left: 87px; top: 503px; width: 792px;
    font-size: 15.5px;
    line-height: 20px;
  }

  .panel-tower { left: 80px; top: 658px; width: 794px; height: 432px; }
  .panel-tower .art {
    left: 276px; top: 9px; right: 8px; bottom: 9px;
    background:
      radial-gradient(ellipse 16% 30% at 48% 55%, rgba(120,160,165,0.75), transparent 70%),
      radial-gradient(ellipse 30% 28% at 45% 22%, rgba(120,100,130,0.7), transparent 70%),
      linear-gradient(90deg, #1e2426 0%, #2c3236 14%, transparent 26%, transparent 72%, #3a3e44 80%, #26262c 100%),
      radial-gradient(ellipse 18% 40% at 10% 45%, rgba(90,35,45,0.6), transparent 70%),
      linear-gradient(180deg, #2f2a34 0%, #3a3442 35%, #2a3034 65%, #1d2c2e 85%, #142022 100%);
  }
  .caption-scene {
    position: absolute;
    left: 26px; top: 30px; width: 232px;
    font-size: 13px;
    line-height: 18.3px;
  }
</style>
</head>
<body>
  <h1 class="story-title">The Amber Lantern</h1>

  <section class="panel panel-city">
    <svg class="frame" viewBox="0 0 796 356" preserveAspectRatio="none" aria-hidden="true">
      <polygon fill="var(--frame)" points="2,4 90,0 200,5 330,1 470,6 600,2 720,5 795,1 793,90 796,180 792,270 795,355 700,352 560,356 420,351 280,355 140,351 40,356 1,353 4,260 0,170 3,80"/>
    </svg>
    <div class="art" role="img" aria-label="Painted dusk view of a ruined Maya city with a stepped pyramid and stone terraces"></div>
    <div class="page-mark">3</div>
  </section>
  <div class="caption-lead">
    <svg viewBox="0 0 310 54" preserveAspectRatio="none" aria-hidden="true">
      <polygon fill="var(--frame)" points="0,1 80,0 180,2 308,0 310,27 307,54 200,52 90,54 2,53 0,28"/>
      <polygon fill="var(--caption)" points="5,4 100,5 200,3 304,5 303,27 305,49 180,48 70,50 6,49 4,26"/>
    </svg>
    <span>These were lawless times.</span>
  </div>

  <p class="narration">
    The kingdoms of Ek were disintegrating. The Maya had greatly displeased the gods, who had punished them since the Spring, when the corn had first gone bad.<br>
    The adventurer had left his own tribes to serve in the emperor’s pay.<br>
    He had been satisfied with good wage; then he lost his taste for slaughtering farmers and peasants.
  </p>

  <section class="panel panel-tower">
    <svg class="frame" viewBox="0 0 794 432" preserveAspectRatio="none" aria-hidden="true">
      <polygon fill="var(--frame)" points="0,2 120,0 260,3 400,0 540,4 680,1 792,3 794,110 791,220 794,330 792,431 650,428 500,432 350,429 200,432 60,429 0,432 2,320 0,210 2,100"/>
      <polygon fill="var(--caption)" points="0,0 90,2 180,0 268,3 265,60 270,130 264,200 269,270 266,362 180,358 90,361 0,359"/>
    </svg>
    <p class="caption-scene">In a tavern earlier that night, the adventurer had overheard a drunken Scythian describe the treasure in Lord Ek’s trove, in particular a necklace of jade ovals. The Scythian had detailed the necklace’s ancient origins and its present location, until he was distracted by a green-eyed serving girl. The young mercenary had decided on the spot to steal it; and now he stood directly below the chambers where the necklace lay.</p>
    <div class="art" role="img" aria-label="Painted view looking up at a towering stone temple facade between dark walls at night"></div>
    <div class="page-mark">2</div>
  </section>
</body>
</html>
```